IT Company Business Card design

Brisk Node is a new computer solutions business focusing on setting up servers and computer systems for small to medium sized businesses.

A business client will either request a solution, or support for a current system and we will turn up on site to provide these services.

We are bast in Christchurch, New Zealand.

We are looking for unique business card's that stand out and show off the business in a professional light.

Open to all idea's etc.

Industry/Entity Type

Computer

Requirements
Must have
• Business Logo (AI file attached)
Employee Name
Business title
Business landline number
Cell phone number
Email
Web URL
Nice to have
• Could be nice to have some keywords (possibly on the back) such as:

Business IT solutions
Network installations
Phone solutions
Server management
Software diagnostics

The above is not needed, just an idea.

```html
<!DOCTYPE html>
<html lang="en">
<head>
<meta charset="utf-8">
<title>Brisk Node – Business Card</title>
<link rel="stylesheet" href="https://fonts.googleapis.com/css2?family=Jost:wght@400;500&display=swap">
<style>
  :root {
    --page: #ffffff;
    --card-light: #f6f6f6;
    --card-edge: #e0e1e2;
    --cyan: #00aeef;
    --blue: #1a75c8;
    --indigo: #2e3a8f;
    --ink: #1d1d1f;
    --muted: #3a3a3c;
    --icon: #1570c0;
    --divider: #4a4a4a;
  }
  html, body {
    margin: 0;
    padding: 0;
    width: 1200px;
    height: 1110px;
    overflow: hidden;
    background: var(--page);
    font-family: "Jost", "Futura", sans-serif;
  }
  .sheet {
    position: relative;
    width: 1085px;
    height: 1003px;
    transform: scale(1.106);
    transform-origin: 0 0;
  }
  .card {
    position: absolute;
    left: 272px;
    width: 652px;
    height: 353px;
    overflow: hidden;
    background: radial-gradient(ellipse at 50% 45%, var(--card-light) 0%, #eeeeef 55%, var(--card-edge) 100%);
  }
  .card--front { top: 115px; }
  .card--back { top: 527px; }

  .accent {
    position: absolute;
    background: linear-gradient(90deg, var(--cyan), var(--blue) 55%, var(--indigo));
  }
  .accent--top {
    left: 0; top: 0;
    width: 240px; height: 10px;
  }
  .accent--bottom {
    right: 0; bottom: 0;
    width: 160px; height: 10px;
    background: linear-gradient(90deg, var(--indigo), var(--blue) 45%, var(--cyan));
  }
  .accent--side {
    left: 0; bottom: 0;
    width: 10px; height: 120px;
    background: linear-gradient(180deg, var(--cyan), var(--blue));
  }

  .holder {
    position: absolute;
    left: 82px;
    top: 37px;
    color: var(--ink);
  }
  .holder__name {
    margin: 0;
    font-size: 21px;
    font-weight: 400;
    letter-spacing: 0.2px;
    line-height: 1.2;
  }
  .holder__title {
    margin: 0;
    font-size: 20px;
    font-weight: 400;
    letter-spacing: 2.6px;
    line-height: 1.3;
    color: var(--muted);
  }
  .contact {
    position: absolute;
    left: 370px;
    top: 208px;
    padding-left: 22px;
    border-left: 2px solid var(--divider);
    color: var(--ink);
    font-size: 19px;
    line-height: 25.5px;
  }
  .contact__row {
    display: flex;
    align-items: center;
    gap: 11px;
  }
  .contact__icon {
    width: 17px;
    height: 17px;
    background: var(--icon);
    color: #fff;
    font-size: 12px;
    font-weight: 500;
    line-height: 17px;
    text-align: center;
  }
  .contact__city {
    margin-top: 4px;
    margin-left: -1px;
  }
  .brand {
    position: absolute;
    left: 198px;
    top: 97px;
    display: flex;
    align-items: center;
    height: 106px;
  }
  .brand__dot {
    width: 100px;
    height: 100px;
    border-radius: 50%;
    background: var(--blue);
  }
  .brand__rule {
    width: 2px;
    height: 106px;
    margin: 0 14px 0 16px;
    background: linear-gradient(to bottom, transparent, var(--divider) 30%, var(--divider) 70%, transparent);
  }
  .brand__name {
    font-size: 36px;
    font-weight: 400;
    letter-spacing: 2px;
    color: var(--ink);
    text-transform: uppercase;
    white-space: nowrap;
  }
</style>
</head>
<body>
<div class="sheet">

  <section class="card card--front">
    <div class="accent accent--top" role="img" aria-label="Blue accent band along the top edge"></div>
    <div class="accent accent--side" role="img" aria-label="Blue accent band along the lower left edge"></div>
    <div class="accent accent--bottom" role="img" aria-label="Blue accent band along the lower right edge"></div>

    <div class="holder">
      <h1 class="holder__name">NAME SURNAME</h1>
      <p class="holder__title">DESIGNATION</p>
    </div>

    <div class="contact">
      <div class="contact__row"><span class="contact__icon">p</span><span>000 000 000</span></div>
      <div class="contact__row"><span class="contact__icon">e</span><span>brisknode@domain.com</span></div>
      <div class="contact__row"><span class="contact__icon">w</span><span>www.brisknode.co.nz</span></div>
      <div class="contact__city">Ashvale New Zealand</div>
    </div>
  </section>

  <section class="card card--back">
    <div class="accent accent--top" role="img" aria-label="Blue accent band along the top edge"></div>
    <div class="accent accent--side" role="img" aria-label="Blue accent band along the lower left edge"></div>
    <div class="accent accent--bottom" role="img" aria-label="Blue accent band along the lower right edge"></div>

    <div class="brand">
      <span class="brand__dot"></span>
      <span class="brand__rule"></span>
      <span class="brand__name">Brisk Node</span>
    </div>
  </section>

</div>
</body>
</html>
```